Browse Every Counter Midtown Harlanby Event

We are hosting a Browse Every Counter Midtown Harlanby event in conjunction with Corvella Charge's Corner Trader Festday. Participants will be given a passport to get stamped at participating businesses. They will be entered to win $$ prizes! I have attached a Word document with the info that needs to be included.

Target Market(s)

Christmas shoppers, mainly women.

Colors
f04a50
31b7a3

Requirements
Must have
• The info attached. Christmas or holiday images.

```html
<!DOCTYPE html>
<html lang="en">
<head>
<meta charset="utf-8">
<title>Browse Every Counter – Midtown Harlanby</title>
<link rel="stylesheet" href="https://fonts.googleapis.com/css2?family=Oswald:wght@400;500;600;700&family=Francois+One&display=swap">
<style>
  :root{
    --maroon:#6f1a14;
    --title-red:#7a1e17;
    --coral:#f04a50;
    --teal:#31b7a3;
    --tan:#d9964a;
    --white:#ffffff;
    --navy:#2a3580;
    --blue:#2f7fc1;
    --green:#3f7d3c;
  }
  *{margin:0;padding:0;box-sizing:border-box}
  html,body{width:846px;height:1200px;overflow:hidden;background:var(--white)}
  .poster{position:relative;width:846px;height:1200px;background:var(--maroon);overflow:hidden;font-family:"Francois One",sans-serif;color:var(--white)}
  .header-band{position:absolute;left:0;top:0;width:846px;height:145px;background:var(--white)}
  .holiday-photo{position:absolute;left:0;top:145px;width:846px;height:460px;
    background:radial-gradient(circle at 62% 60%,#c43a2c 0%,#8a2a1c 22%,transparent 45%),
               radial-gradient(circle at 85% 25%,#3b5a2a 0%,transparent 40%),
               linear-gradient(135deg,#1b2a17 0%,#2c3f22 45%,#3a2a1a 100%);
    clip-path:polygon(0 0,100% 0,100% 64%,47% 100%,0 100%)}
  .date-panel{position:absolute;left:62px;top:145px;width:338px;height:400px;background:var(--tan)}
  .event-date{position:absolute;left:92px;top:358px;font-family:"Oswald",sans-serif;font-weight:700;color:var(--title-red);font-size:28px;line-height:1.25;text-transform:uppercase;letter-spacing:.2px}
  .event-date .day{font-size:50px;line-height:1}
  .event-date sup{font-size:24px;vertical-align:22px;text-transform:none}
  .event-date .time{font-size:31px}
  .shield{position:absolute;left:45px;top:-6px;width:362px;height:336px}
  .shield-title{position:absolute;left:45px;top:32px;width:362px;text-align:center;font-family:"Oswald",sans-serif;font-weight:700;color:var(--title-red);font-size:46px;line-height:1.1;text-transform:uppercase}
  .shield-star{position:absolute;left:216px;top:150px;width:20px;height:20px}
  .client-name{position:absolute;left:45px;top:206px;width:362px;text-align:center;font-family:"Oswald",sans-serif;font-weight:600;color:var(--green);font-size:30px;text-transform:uppercase;letter-spacing:1px;line-height:1.1}
  .partner{position:absolute;top:40px;display:flex;align-items:center;gap:8px;font-family:"Oswald",sans-serif;font-weight:600;font-size:16px;line-height:1.15;text-transform:uppercase}
  .partner-charge{left:448px;color:var(--navy)}
  .partner-fest{left:604px;color:var(--blue)}
  .partner .dot{width:62px;height:62px;border-radius:50%;background:var(--navy);flex:none}
  .partner .box{width:58px;height:58px;background:var(--blue);flex:none}
  .offer-card{position:absolute;left:45px;top:480px;width:363px;height:600px}
  .offer-text{position:absolute;left:45px;top:563px;width:363px;text-align:center;font-size:26px;line-height:1.3}
  .offer-text .big{font-size:44px;vertical-align:-4px}
  .divider{display:block;margin:22px auto;width:270px;height:20px}
  .sponsors{position:absolute;left:418px;top:620px;width:405px;text-align:center;font-size:20px;line-height:41.5px}
  .sponsors h2{font-family:"Oswald",sans-serif;font-weight:600;font-size:30px;text-decoration:underline;text-underline-offset:6px;margin-bottom:6px;line-height:44px}
  .fine-print{position:absolute;left:0;top:1121px;width:846px;text-align:center;font-family:"Oswald",sans-serif;font-weight:400;font-size:15px;line-height:1.35}
  .teal-strip{position:absolute;left:0;bottom:0;width:846px;height:18px;background:var(--teal)}
</style>
</head>
<body>
<main class="poster">
  <div class="header-band"></div>
  <div class="holiday-photo" role="img" aria-label="Wrapped holiday gift boxes with ribbons beneath a lit Christmas tree with red ornaments"></div>

  <div class="date-panel"></div>

  <svg class="shield" viewBox="0 0 362 336" aria-hidden="true">
    <path d="M2 0 V290 L181 334 L360 290 V0" fill="var(--white)" stroke="var(--teal)" stroke-width="4"/>
  </svg>
  <h1 class="shield-title">Browse Every<br>Counter</h1>
  <svg class="shield-star" viewBox="0 0 20 20" aria-hidden="true"><polygon points="10,0 12.9,6.9 20,7.6 14.6,12.3 16.2,20 10,16 3.8,20 5.4,12.3 0,7.6 7.1,6.9" fill="var(--tan)"/></svg>
  <p class="client-name">Midtown Harlanby</p>

  <div class="partner partner-charge"><span class="dot"></span><span>Corvella<br>Charge</span></div>
  <div class="partner partner-fest"><span class="box"></span><span>Corner Trader<br>Festday</span></div>

  <p class="event-date">November <span class="day">27</span><sup>th</sup>, 2021<br><span class="time">10:00 A.M. - 2:00 P.M.</span></p>

  <svg class="offer-card" viewBox="0 0 363 600" aria-hidden="true">
    <path d="M0 60 L340 0 L363 10 V570 Q363 600 333 600 H30 Q0 600 0 570 Z" fill="var(--coral)"/>
  </svg>
  <div class="offer-text">
    <p>Enter to win <span class="big">$500</span><br>in Shopping Dollars<br>&amp; other gift giveaways!*</p>
    <svg class="divider" viewBox="0 0 270 20" aria-hidden="true"><line x1="0" y1="10" x2="105" y2="10" stroke="var(--maroon)" stroke-width="3"/><polygon points="135,0 138,7 145,7.5 139.5,12 141.5,20 135,15.5 128.5,20 130.5,12 125,7.5 132,7" fill="var(--maroon)"/><line x1="165" y1="10" x2="270" y2="10" stroke="var(--maroon)" stroke-width="3"/></svg>
    <p>Get Your Pictures with<br>Harlanby's Yule Visitor</p>
    <svg class="divider" viewBox="0 0 270 20" aria-hidden="true"><line x1="0" y1="10" x2="105" y2="10" stroke="var(--maroon)" stroke-width="3"/><polygon points="135,0 138,7 145,7.5 139.5,12 141.5,20 135,15.5 128.5,20 130.5,12 125,7.5 132,7" fill="var(--maroon)"/><line x1="165" y1="10" x2="270" y2="10" stroke="var(--maroon)" stroke-width="3"/></svg>
    <p>Enter to win ONE of FIVE<br>$250 Shopping Dollars!<br>Pick up your FREE<br>Tote &amp; Passport at the Depot</p>
  </div>

  <section class="sponsors">
    <h2>SPONSORED BY</h2>
    <p>Dusk Street Nights</p>
    <p>Harlanby Acorn Fair,</p>
    <p>R. Dell's Crafted Layouts</p>
    <p>Ferris County Chamber &amp; Visitors</p>
    <p>Owen Castell Photography</p>
    <p>Tarrow Power Cooperative</p>
    <p>Harlanby Midtown Development</p>
    <p>The Daily Ledger</p>
    <p>Wave 98.7 FM/AM 1320</p>
    <p>Harlanby's Yule Visitor</p>
  </section>

  <p class="fine-print">For more information, contact Avery Lane, 555-014-2290<br>*Eligible to be entered to win when stamps from all participating stores reflected on Browse Every Counter Passport</p>
  <div class="teal-strip"></div>
</main>
</body>
</html>
```